Business Card Design Project

Need a business card with logo that is attached.
Company name: Tolmen Brisk Solutions, LLC
My name: Lorna Tolmen
Title: President
Phone number: 703-555-0148
Email: ltolmen@tolmenbrisksolutions.example
web site: www.tolmenbrisksolutions.example

Industry/Entity Type

Business

```html
<!DOCTYPE html>
<html lang="en">
<head>
<meta charset="utf-8">
<title>Tolmen Brisk Solutions, LLC — Business Card</title>
<link rel="stylesheet" href="https://fonts.googleapis.com/css2?family=Cinzel:wght@400;500&family=Arimo:wght@400&display=swap">
<style>
  :root {
    --backdrop: #cdb79c;
    --card: #141414;
    --brand-blue: #1e6fb8;
    --brand-teal: #13876f;
    --rule: #4a4a4a;
    --text-light: #f2f2f2;
    --band-blue: #1a6db5;
    --band-teal: #12806b;
  }
  * { box-sizing: border-box; margin: 0; padding: 0; }
  html, body {
    width: 1200px; height: 646px; overflow: hidden;
    background: var(--backdrop);
  }
  .card {
    position: absolute; left: 150px; top: 66px;
    width: 900px; height: 514px;
    background: var(--card);
    overflow: hidden;
    box-shadow: 0 14px 30px rgba(0,0,0,0.35);
  }
  .brand-mark {
    position: absolute; left: 62px; top: 96px;
    width: 124px; height: 124px; border-radius: 50%;
    background: var(--brand-blue);
  }
  .brand-divider {
    position: absolute; left: 214px; top: 74px;
    width: 3px; height: 170px; background: var(--brand-teal);
  }
  .company-name {
    position: absolute; left: 236px; top: 70px;
    font-family: "Cinzel", serif; font-weight: 500;
    font-size: 40px; line-height: 44px; letter-spacing: 1px;
    color: var(--brand-blue); text-transform: uppercase;
  }
  .rule {
    position: absolute; height: 1px; background: var(--rule);
  }
  .rule--name { left: 236px; top: 204px; width: 624px; }
  .rule--contact { left: 60px; top: 292px; width: 800px; }
  .person-name {
    position: absolute; left: 470px; top: 168px;
    font-family: "Cinzel", serif; font-size: 28px; letter-spacing: 1px;
    color: var(--brand-blue); text-transform: uppercase;
  }
  .person-title {
    position: absolute; left: 492px; top: 212px;
    font-family: "Cinzel", serif; font-size: 20px; letter-spacing: 1px;
    color: var(--brand-teal); text-transform: uppercase;
  }
  .contact-list {
    position: absolute; left: 64px; top: 314px; list-style: none;
  }
  .contact-item {
    display: flex; align-items: center; gap: 22px;
    height: 48px;
    font-family: "Arimo", sans-serif; font-size: 23px;
    color: var(--text-light);
  }
  .contact-icon { width: 22px; height: 22px; flex: none; }
  .band-blue {
    position: absolute; left: 0; bottom: 0; width: 100%; height: 34px;
    background: var(--band-blue);
  }
  .band-teal {
    position: absolute; right: 0; bottom: 0; width: 118px; height: 34px;
    background: var(--band-teal);
    clip-path: polygon(10px 0, 100% 0, 100% 100%, 0 100%);
  }
  .band-notch {
    position: absolute; right: 118px; bottom: 0; width: 14px; height: 34px;
    background: var(--card);
    clip-path: polygon(10px 0, 14px 0, 4px 100%, 0 100%);
  }
</style>
</head>
<body>
  <div class="card">
    <div class="brand-mark"></div>
    <div class="brand-divider"></div>
    <div class="company-name">Tolmen Brisk<br>Solutions,<br>LLC</div>

    <div class="rule rule--name"></div>
    <div class="person-name">Lorna Tolmen</div>
    <div class="person-title">President</div>

    <div class="rule rule--contact"></div>
    <ul class="contact-list">
      <li class="contact-item">
        <svg class="contact-icon" viewBox="0 0 24 24" aria-hidden="true">
          <path fill="#13876f" d="M6.6 10.8a15 15 0 0 0 6.6 6.6l2.2-2.2c.3-.3.7-.4 1-.2 1.1.4 2.3.6 3.6.6.6 0 1 .4 1 1V20c0 .6-.4 1-1 1C10.6 21 3 13.4 3 4c0-.6.4-1 1-1h3.5c.6 0 1 .4 1 1 0 1.3.2 2.5.6 3.6.1.3 0 .7-.2 1z"/>
        </svg>
        <span>703-555-0148</span>
      </li>
      <li class="contact-item">
        <svg class="contact-icon" viewBox="0 0 24 24" aria-hidden="true">
          <rect x="2" y="5" width="20" height="14" rx="2" fill="#13876f"/>
          <path d="M3 6l9 7 9-7" fill="none" stroke="#141414" stroke-width="1.8"/>
        </svg>
        <span>ltolmen@tolmenbrisksolutions.example</span>
      </li>
      <li class="contact-item">
        <svg class="contact-icon" viewBox="0 0 24 24" aria-hidden="true">
          <circle cx="12" cy="12" r="10" fill="#13876f"/>
          <g fill="none" stroke="#141414" stroke-width="1.4">
            <ellipse cx="12" cy="12" rx="4.5" ry="10"/>
            <path d="M2 12h20M4 7h16M4 17h16"/>
          </g>
        </svg>
        <span>www.tolmenbrisksolutions.example</span>
      </li>
    </ul>

    <div class="band-blue"></div>
    <div class="band-notch"></div>
    <div class="band-teal"></div>
  </div>
</body>
</html>
```